Self Storage Postcard

We need a general postcard designed that can be handed out or mailed. There will need to be room on the back of the postcard for postage and address. See template.

Website: https://www.boxvaultly.com/unit-rentals-manteca-ca-k8251
Updates

Please dont use the Crate N Keep logo as that company has nothing to do with Crate N Keep. Please see the Crate N Keep logo that was provided. Thanks

Target Market(s)

Potential Self Storage Tenants

Industry/Entity Type

Self Storage

Font styles to use
Sans Serif

Requirements
Must have
• $1.00 Move In Special

```html
<!DOCTYPE html>
<html lang="en">
<head>
<meta charset="utf-8">
<title>Crate N Keep Postcard</title>
<link href="https://fonts.googleapis.com/css2?family=Montserrat:wght@400;600;800;900&family=Lato:ital,wght@0,400;0,700;1,400&display=swap" rel="stylesheet">
<style>
:root{
  --bg:#666666;
  --blue:#1f73b7;
  --orange:#f39322;
  --ink:#1d1d1d;
  --white:#ffffff;
  --stamp:#e6e6e6;
}
*{box-sizing:border-box;margin:0;padding:0}
html,body{width:1197px;height:1200px;overflow:hidden;background:var(--bg)}
body{position:relative;font-family:'Lato',sans-serif;color:var(--ink)}
.card{position:absolute;width:804px;height:441px;background:var(--white);overflow:hidden;box-shadow:0 2px 6px rgba(0,0,0,.35)}
.card--front{left:132px;top:118px}
.card--back{left:306px;top:613px;width:802px}

/* brand */
.brand{display:flex;align-items:center;position:absolute}
.brand__mark{background:var(--blue);flex:none}
.brand__name{font-family:'Montserrat',sans-serif;font-weight:800;color:var(--blue);white-space:nowrap;line-height:1}

/* front */
.hero-photo{position:absolute;left:0;top:0;width:426px;height:441px;
  background:linear-gradient(110deg,#5d7a3a 0%,#3b5a9b 28%,#c9b08a 55%,#e8e4dc 75%,#6d5a48 100%)}
.front-panel{position:absolute;left:426px;top:0;width:378px;height:441px}
.front-panel .brand{left:73px;top:19px;gap:10px}
.front-panel .brand__mark{width:48px;height:48px}
.front-panel .brand__name{font-size:25px}
.headline-band{position:absolute;left:0;top:88px;width:378px;height:82px;background:var(--blue);
  color:var(--white);font-family:'Montserrat',sans-serif;font-weight:900;font-size:25.5px;text-align:center;line-height:32px;padding-top:10px}
.headline-band::after{content:"";position:absolute;left:50%;bottom:-12px;margin-left:-14px;border-left:14px solid transparent;border-right:14px solid transparent;border-top:12px solid var(--blue)}
.tagline{position:absolute;left:21px;top:182px;font-family:'Montserrat',sans-serif;font-weight:800;font-size:21px}
.tagline em{font-style:normal;color:var(--orange)}
.subline{position:absolute;left:30px;top:210px;font-family:'Montserrat',sans-serif;font-size:21px;font-weight:400}
.features{position:absolute;left:31px;top:244px;list-style:none;font-family:'Montserrat',sans-serif;font-size:11px;font-weight:600}
.features li{display:flex;align-items:center;gap:8px;height:20px}
.features svg{width:12px;height:12px}
.about{position:absolute;left:21px;top:309px;width:334px;font-size:8.6px;line-height:11px;text-align:justify}
.guarantee{position:absolute;left:21px;top:357px;width:340px;color:var(--blue);font-weight:700;font-size:15.5px;line-height:18px}
.url-bar{position:absolute;left:0;top:404px;width:378px;height:37px;background:var(--orange);color:var(--white);
  font-weight:700;font-size:11.5px;display:flex;align-items:center;justify-content:center}

/* back */
.offer-panel{position:absolute;left:0;top:0;width:432px;height:357px;background:var(--blue);color:var(--white)}
.offer-badge{position:absolute;left:26px;top:28px;width:392px;height:65px;background:var(--orange);border-radius:14px;
  display:flex;align-items:center;justify-content:center;gap:8px;font-family:'Montserrat',sans-serif;font-weight:800}
.offer-badge::before{content:"";position:absolute;inset:4px;border:1.5px dashed var(--white);border-radius:11px}
.offer-badge__price{font-size:50px;font-weight:900;letter-spacing:-2px}
.offer-badge__text{font-size:37px}
.offer-terms{position:absolute;left:0;top:98px;width:432px;text-align:center;font-family:'Montserrat',sans-serif;font-weight:800;font-size:13.5px}
.offer-copy{position:absolute;left:27px;top:129px;width:392px;font-size:14.3px;line-height:17px}
.offer-cta{position:absolute;left:27px;top:254px;font-size:18px}
.contact{position:absolute;left:26px;display:flex;align-items:center;gap:10px;font-family:'Montserrat',sans-serif;font-weight:800}
.contact--phone{top:283px;font-size:34px}
.contact--address{top:324px;font-size:15px;left:30px}
.contact svg{flex:none}
.map{position:absolute;left:0;top:357px;width:239px;height:84px;background:linear-gradient(135deg,#eef0f3,#dfe5ea)}
.review{position:absolute;left:245px;top:361px;width:188px;font-size:7.4px;line-height:9.6px;font-style:italic}
.review__author{color:var(--orange);font-size:8px;margin-top:3px}
.review__author small{font-size:4.5px}
.stars{display:flex;gap:2px;margin-top:4px}
.address-side .brand{left:449px;top:22px;gap:6px}
.address-side .brand__mark{width:28px;height:28px}
.address-side .brand__name{font-size:15px}
.return-label{position:absolute;left:484px;top:58px;font-size:12px}
.stamp-box{position:absolute;left:726px;top:22px;width:53px;height:63px;background:var(--stamp)}
.address-line{position:absolute;left:600px;width:184px;height:1px;background:#333}
</style>
</head>
<body>

<section class="card card--front">
  <div class="hero-photo" role="img" aria-label="Photo of a smiling mover in a blue cap lifting cardboard boxes into a truck"></div>
  <div class="front-panel">
    <div class="brand"><span class="brand__mark"></span><span class="brand__name">CRATE N KEEP</span></div>
    <div class="headline-band">SAVE MONEY, SAVE TIME<br>RENT ONLINE</div>
    <p class="tagline">Self- Storage <em>Delivered</em> to you</p>
    <p class="subline">it doesn’t get easier than that</p>
    <ul class="features">
      <li><svg viewBox="0 0 12 12"><rect x="1" y="2" width="9" height="9" fill="none" stroke="#f39322" stroke-width="1.3"/><path d="M3 6l2.5 2.5L11 1.5" fill="none" stroke="#f39322" stroke-width="1.8"/></svg>ALL LOCATIONS : Find Self Storage Near You</li>
      <li><svg viewBox="0 0 12 12"><rect x="1" y="2" width="9" height="9" fill="none" stroke="#f39322" stroke-width="1.3"/><path d="M3 6l2.5 2.5L11 1.5" fill="none" stroke="#f39322" stroke-width="1.8"/></svg>PAY ONLINE : Manage Your Account</li>
      <li><svg viewBox="0 0 12 12"><rect x="1" y="2" width="9" height="9" fill="none" stroke="#f39322" stroke-width="1.3"/><path d="M3 6l2.5 2.5L11 1.5" fill="none" stroke="#f39322" stroke-width="1.8"/></svg>SIZE GUIDE : Calculate the storage size you need</li>
    </ul>
    <p class="about">We provides safe and secure storage in a convenient, clean, and professionally managed operation that exceeds our customer’s expectations. Whether you’re looking for temporary storage or a more permanent solution, one of our helpful .professionals can guide you through the process</p>
    <p class="guarantee">We take your satisfaction so seriously that we offer a 100% satisfaction guarantee</p>
    <div class="url-bar">https://www.boxvaultly.com/unit-rentals-manteca-ca-k8251</div>
  </div>
</section>

<section class="card card--back">
  <div class="offer-panel">
    <div class="offer-badge"><span class="offer-badge__price">$1</span><span class="offer-badge__text">Move-In Special</span></div>
    <p class="offer-terms">On 1st Full Month's Rent*Subject to availability</p>
    <p class="offer-copy">Moving to a new home or office in Manteca, CA? You’ll need some extra space - and we have all the space you need at Crate N Keep! You’ll find our facility at 1186 Larkspur Cir near the Crestview Plaza Shopping Center. We’re near the intersection of CA-120 and Main Street, so we’re easy to find and access from nearly any part of Manteca. We’re just a short drive from Salida, Ripon, Tracy, French Camp, and Lathrop, CA</p>
    <p class="offer-cta">Let us help you reserve your storage unit today</p>
    <div class="contact contact--phone">
      <svg width="26" height="26" viewBox="0 0 26 26"><circle cx="13" cy="13" r="11.5" fill="none" stroke="#f39322" stroke-width="2"/><path d="M9 7.5c-1 1-1.3 3 .5 5.8s4 4.4 5.5 4.7c1.2.2 2-.5 2.5-1.3l-2-1.8-1.3 1c-1.2-.5-2.8-2.2-3.4-3.5l1-1.3-1.7-2.2z" fill="#f39322"/></svg>
      209.555.0147
    </div>
    <div class="contact contact--address">
      <svg width="14" height="18" viewBox="0 0 14 18"><path d="M7 0a7 7 0 0 0-7 7c0 5 7 11 7 11s7-6 7-11a7 7 0 0 0-7-7z" fill="#f39322"/><circle cx="7" cy="7" r="2.6" fill="#1f73b7"/></svg>
      1186 Larkspur Circle Manteca, CA 95337
    </div>
  </div>
  <div class="map" role="img" aria-label="Street map showing the facility location near the shopping center"></div>
  <div class="review">
    “ Our occupancy rates and profitability have gone up significantly since BoxVaultly took over managing and marketing our properties. We get far better results for less expense than when we were doing it ourselves ”
    <p class="review__author">Dana Whitlock, <small>Riverbend Storage Partners client since 1998</small></p>
    <div class="stars">
      <svg width="66" height="11" viewBox="0 0 66 11"><g fill="#f5c518"><path id="st" d="M5.5 0l1.6 3.5 3.9.4-2.9 2.6.8 3.8-3.4-2-3.4 2 .8-3.8L0 3.9l3.9-.4z"/><use href="#st" x="13.5"/><use href="#st" x="27"/><use href="#st" x="40.5"/><use href="#st" x="54"/></g></svg>
    </div>
  </div>
  <div class="address-side">
    <div class="brand"><span class="brand__mark"></span><span class="brand__name">CRATE N KEEP</span></div>
    <p class="return-label">Return address to</p>
    <div class="stamp-box"></div>
    <div class="address-line" style="top:207px"></div>
    <div class="address-line" style="top:230px"></div>
    <div class="address-line" style="top:253px"></div>
  </div>
</section>

</body>
</html>
```